RB Cargonet businesscard project

RB Cargonet Ltd is a freshly founded small (3 employees), young (average age is 30 years) company, living from the road transportation market without own tools.
We would like to have an impressive, new-line, cool busines card for a freshly founded forwarding company on an overcrowded market which raises attention and makes the potential partners eager to work with us.

Our logo is in the attachment, please use it for the card.

Target Market(s)

The main profile of the company is logistic/forwarding on road.

Industry/Entity Type

Freight Forwarding

Contact Information for Business Card

Name: Varga Edina
Title: general manager
mobile nr: +36-70/482-5910
fax nr: +36-1/655-3947
e-mail: edina.varga@rbcargonet-example.com
info@rbcargonet-example.com
website address: http://www.rbcargonet-example.com
and if possible maybe some funny or helpful info on the back

Requirements
Must have
• contact details above
Nice to have
• some really nice and catching back-side (info, graphics, useful tool info... anything)
Should not have
• trucks, road, ship, airplane on it...

```html
<!DOCTYPE html>
<html lang="en">
<head>
<meta charset="utf-8">
<title>RB Cargonet – Business Card</title>
<link rel="stylesheet" href="https://fonts.googleapis.com/css2?family=Arimo:wght@400&family=Open+Sans:wght@400;700&family=Oswald:wght@400&display=swap">
<style>
  :root {
    --page-bg: #2b2b2b;
    --card-white: #ffffff;
    --card-mist: #e6e7e9;
    --panel-dark: #232323;
    --brand-blue: #4f7fbf;
    --text-dark: #2a2a2a;
    --text-light: #ffffff;
  }
  * { margin: 0; padding: 0; box-sizing: border-box; }
  html, body {
    width: 1200px; height: 947px; overflow: hidden;
    background: var(--page-bg);
  }
  .card {
    position: absolute; left: 100px; top: 188px;
    width: 1000px; height: 571px;
    overflow: hidden;
    background: var(--card-white);
    box-shadow: 0 10px 30px rgba(0,0,0,.5);
    font-family: "Arimo", Arial, sans-serif;
  }
  .card-shapes { position: absolute; inset: 0; width: 100%; height: 100%; }

  .brand {
    position: absolute; left: 90px; top: 178px;
    display: flex; align-items: center; gap: 16px;
  }
  .brand-square { width: 40px; height: 40px; background: var(--brand-blue); }
  .brand-name {
    font-family: "Oswald", "Arial Narrow", sans-serif;
    font-weight: 400; font-size: 50px; color: var(--text-dark);
    line-height: 1;
  }

  .services {
    position: absolute; left: 610px; top: 52px;
    list-style: none;
    font-size: 27px; color: var(--text-dark); line-height: 35px;
  }
  .services li { display: flex; align-items: center; }
  .services li::before {
    content: ""; width: 0; height: 0; margin-right: 14px;
    border-left: 11px solid var(--brand-blue);
    border-top: 6px solid transparent; border-bottom: 6px solid transparent;
  }

  .person {
    position: absolute; right: 70px; top: 338px;
    text-align: right; color: var(--text-light);
    padding-right: 22px; border-right: 3px solid var(--brand-blue);
  }
  .person-name {
    font-family: "Open Sans", Arial, sans-serif;
    font-weight: 700; font-size: 34px; line-height: 34px;
  }
  .person-title { font-size: 18px; line-height: 20px; }

  .tagline {
    position: absolute; left: 520px; top: 448px;
    font-size: 27px; color: var(--text-light);
  }

  .contacts {
    position: absolute; left: 66px; top: 378px;
    list-style: none; color: var(--text-light);
    font-size: 19px; line-height: 22px;
  }
  .contacts li { display: flex; align-items: flex-start; margin-bottom: 10px; }
  .contacts svg { width: 18px; height: 18px; margin-right: 16px; margin-top: 3px; flex: none; }
  .contacts .stack { display: flex; flex-direction: column; }
</style>
</head>
<body>
<div class="card">
  <svg class="card-shapes" viewBox="0 0 1000 571" preserveAspectRatio="none" aria-hidden="true">
    <defs>
      <linearGradient id="mist" x1="0" y1="0" x2="1" y2="1">
        <stop offset="0" stop-color="#f3f4f5"/>
        <stop offset="0.45" stop-color="#ffffff"/>
        <stop offset="0.75" stop-color="#e8e9eb"/>
        <stop offset="1" stop-color="#f7f7f8"/>
      </linearGradient>
    </defs>
    <rect class="mist-field" width="1000" height="340" fill="url(#mist)" role="img" aria-label="Soft grey swirl background"/>
    <polygon class="accent-strip" points="0,318 590,318 615,340 0,340" fill="var(--brand-blue)"/>
    <polygon class="dark-panel" points="0,340 620,340 650,300 1000,300 1000,571 0,571" fill="var(--panel-dark)"/>
    <polygon class="tagline-band" points="460,498 490,440 1000,440 1000,498" fill="var(--brand-blue)"/>
  </svg>

  <div class="brand">
    <span class="brand-square"></span>
    <span class="brand-name">RB Cargonet</span>
  </div>

  <ul class="services">
    <li>Air Freight</li>
    <li>Ocean Freight</li>
    <li>Sea-Air Freight</li>
    <li>Freight Insurance</li>
  </ul>

  <div class="person">
    <div class="person-name">Varga Edina</div>
    <div class="person-title">General Manager</div>
  </div>

  <div class="tagline">Fast, reliable and cost-effective</div>

  <ul class="contacts">
    <li>
      <svg viewBox="0 0 18 18" aria-hidden="true"><rect x="4" y="1" width="10" height="16" rx="2" fill="none" stroke="#fff" stroke-width="2"/><rect x="7.5" y="13" width="3" height="2" fill="#fff"/></svg>
      <span>+36-70/482-5910</span>
    </li>
    <li>
      <svg viewBox="0 0 18 18" aria-hidden="true"><rect x="4" y="1" width="10" height="6" fill="#fff"/><rect x="1" y="7" width="16" height="7" rx="1" fill="#fff"/><rect x="4" y="12" width="10" height="5" fill="#fff" stroke="#232323" stroke-width="1"/></svg>
      <span>+36-1/655-3947</span>
    </li>
    <li>
      <svg viewBox="0 0 18 18" aria-hidden="true"><rect x="1" y="4" width="16" height="11" fill="#fff"/><path d="M1 4 L9 10 L17 4" fill="none" stroke="#232323" stroke-width="1.5"/></svg>
      <span class="stack"><span>edina.varga@rbcargonet-example.com</span><span>info@rbcargonet-example.com</span></span>
    </li>
    <li>
      <svg viewBox="0 0 18 18" aria-hidden="true"><circle cx="9" cy="9" r="7.5" fill="none" stroke="#fff" stroke-width="1.5"/><ellipse cx="9" cy="9" rx="3" ry="7.5" fill="none" stroke="#fff" stroke-width="1.2"/><line x1="1.5" y1="9" x2="16.5" y2="9" stroke="#fff" stroke-width="1.2"/></svg>
      <span>www.rbcargonet-example.com</span>
    </li>
  </ul>
</div>
</body>
</html>
```